Design for a 3-4 screens mobile app

The app is a "simple" ordering mobile app.
1. START screen : user can select either "NEW order" either "VIEW history" - or, can access the usual Contact, About, and Conditions pages.
2. NEW order : is a sequence of 3 basic screens/forms made of 3-4 fields each. Logic is the following: you select the service you need, its recurrence, mention where you are located and then you post it towards the marketplace...
3. VIEW history : is where you land at the end of the ordering process - and accessible from START screen. You see there your previous orders, and their statuses.
Mandatory : we need design for START screen, NEW order and VIEW history screens.
Design but be optimized for Smartphones, used in Portrait mode.
Please take into account the design of the website promoting the Mobile App: https://tidyvanlane.be/
Optional but of course nice to have if you could propose some design or guidance for Contact, About, and Conditions pages...
Here attached a full screen sequence.
Updates
Thanks for all your proposals ! They were submitted to the final customer, he selects one ASAP !
Number of Pages Required
3 page
Look and feel
Each slider illustrates characteristics of the customer's brand and the style your logo design should communicate.

```html
<!DOCTYPE html>
<html lang="en">
<head>
<meta charset="utf-8">
<title>Tidy Van Lane – App Screens</title>
<link rel="stylesheet" href="https://fonts.googleapis.com/css2?family=Montserrat:wght@300;400;500;600;700&display=swap">
<style>
:root{
  --stage-dark:#6e4127;
  --stage-light:#8a5635;
  --orange-deep:#dd5400;
  --orange-mid:#e8680f;
  --orange-soft:#f0915a;
  --circle:#b94600;
  --brown-title:#8c2f00;
  --white:#ffffff;
  --cream:#fff3ea;
  --green:#1fa34a;
  --refuse:#5c2608;
  --bar:#ffffff;
  --ink:#222222;
}
*{box-sizing:border-box;margin:0;padding:0}
html,body{width:1200px;height:730px;overflow:hidden}
body{
  font-family:"Montserrat",sans-serif;
  background:radial-gradient(ellipse at 50% 40%,var(--stage-light),var(--stage-dark));
  position:relative;color:var(--white);
}
.screen{
  position:absolute;top:54px;width:350px;height:622px;overflow:hidden;
  background:linear-gradient(155deg,var(--orange-deep) 0%,var(--orange-mid) 55%,#ee7a35 100%);
}
.screen--contact{left:42px}
.screen--order{left:425px}
.screen--status{left:808px}
.status-bar{
  height:21px;background:var(--bar);color:var(--ink);
  display:flex;align-items:center;justify-content:space-between;
  padding:0 28px 0 30px;font-size:11px;font-weight:500;
}
.status-bar .time{font-weight:600;margin-left:14px}
.status-bar .battery{width:22px;height:7px;background:var(--ink);border-radius:1px;position:relative}
.status-bar .battery::after{content:"";position:absolute;right:-2px;top:2px;width:1.5px;height:3px;background:var(--ink)}
.carrier{display:flex;align-items:center;gap:4px}
.abs{position:absolute}
.center-x{left:0;right:0;text-align:center}

/* contact screen */
.brand-mark{left:123px;top:50px;width:105px;height:105px;background:#f5923a}
.brand-name{top:172px;font-size:15px;font-weight:700}
.welcome{left:66px;width:225px;top:196px;font-size:8.3px;line-height:13px;font-weight:400}
.dots{left:77px;width:196px;top:235px;border-top:1px dotted rgba(255,255,255,.7)}
.hex{left:150px;width:52px;height:48px}
.contact-label{font-size:11px;font-weight:400}
.contact-value{font-size:17.5px;font-weight:500}

/* order screen */
.top-band{left:0;right:0;top:21px;height:49px;background:linear-gradient(90deg,#e8701f,var(--orange-soft))}
.back-btn{left:30px;top:26px;width:38px;height:39px;background:var(--white);color:var(--orange-deep);
  font-size:6px;font-weight:600;text-align:center;padding-top:5px}
.back-btn svg{display:block;margin:0 auto 2px}
.nav-hex{top:33px;width:25px;height:24px}
.row-icon{left:73px;width:35px;height:35px;border-radius:50%;background:var(--circle);
  display:flex;align-items:center;justify-content:center}
.row-text{left:115px;font-size:11px;line-height:13.5px}
.row-text b{font-weight:700}
.row-text .cap{font-size:9px;font-weight:700;display:block}
.row-text .big{font-size:17px;font-weight:400;display:block;line-height:18px}
.rule{left:78px;width:229px;border-top:1px solid rgba(255,255,255,.4)}
.send-btn{left:73px;width:205px;top:531px;height:31px;background:var(--white);color:var(--orange-deep);
  font-size:10px;font-weight:700;display:flex;align-items:center;justify-content:center;letter-spacing:.3px}

/* status screen */
.status-title{top:35px;font-size:18px;font-weight:300;letter-spacing:.5px}
.job-icon{left:31px;width:55px;height:55px;border-radius:50%;background:var(--circle);
  display:flex;align-items:center;justify-content:center}
.job-title{left:96px;font-size:12px;font-weight:700;color:var(--brown-title)}
.job-line{left:96px;font-size:9.5px;font-weight:400}
.pending{left:238px;top:204px;display:flex;align-items:center;gap:5px;font-size:8.5px;letter-spacing:.4px}
.pending .ring{width:27px;height:27px;border-radius:50%;border:1px dotted var(--white);
  display:flex;align-items:center;justify-content:center;font-size:8px}
.btn{left:73px;width:204px;height:30px;display:flex;align-items:center;justify-content:center;
  font-size:10px;font-weight:700;letter-spacing:.6px}
.btn--accept{top:429px;background:var(--green)}
.btn--refuse{top:478px;background:var(--refuse)}
</style>
</head>
<body>

<!-- Contact screen -->
<section class="screen screen--contact">
  <div class="status-bar"><span class="carrier">Carrier
    <svg width="11" height="8" viewBox="0 0 11 8"><path d="M5.5 8 L0 2.5 A8 8 0 0 1 11 2.5Z" fill="#222"/></svg></span>
    <span class="time">2:32 PM</span><span class="battery"></span></div>
  <div class="abs brand-mark"></div>
  <div class="abs center-x brand-name">Tidy Van Lane</div>
  <p class="abs welcome">Welcome on Tidy Van Lane, should you have any question about this App or our services, do not hesitate to</p>
  <div class="abs dots"></div>

  <svg class="abs hex" style="top:259px" viewBox="0 0 52 48"><polygon points="13,1 39,1 51,24 39,47 13,47 1,24" fill="none" stroke="#fff" stroke-width="1.3"/>
    <path d="M18 17c0 8 7 15 15 15l3-3-4-3-2 2c-3-1-6-4-7-7l2-2-3-4z" fill="none" stroke="#fff" stroke-width="1.2"/></svg>
  <div class="abs center-x contact-label" style="top:314px">Call us on</div>
  <div class="abs center-x contact-value" style="top:330px">+32 470 28 41 06</div>

  <svg class="abs hex" style="top:385px" viewBox="0 0 52 48"><polygon points="13,1 39,1 51,24 39,47 13,47 1,24" fill="none" stroke="#fff" stroke-width="1.3"/>
    <rect x="16" y="17" width="20" height="14" fill="none" stroke="#fff" stroke-width="1.2"/><path d="M16 17l10 8 10-8M16 31l7-7M36 31l-7-7" fill="none" stroke="#fff" stroke-width="1.2"/></svg>
  <div class="abs center-x contact-label" style="top:437px">Sends us an email at</div>
  <div class="abs center-x contact-value" style="top:453px">info@tidyvanlane.be</div>

  <svg class="abs hex" style="top:505px" viewBox="0 0 52 48"><polygon points="13,1 39,1 51,24 39,47 13,47 1,24" fill="none" stroke="#fff" stroke-width="1.3"/>
    <path d="M17 23l18-7-7 18-3-8z" fill="none" stroke="#fff" stroke-width="1.2"/></svg>
  <div class="abs center-x contact-label" style="top:561px">Visit our Website at</div>
  <div class="abs center-x contact-value" style="top:577px">tidyvanlane.be</div>
</section>

<!-- New order screen -->
<section class="screen screen--order">
  <div class="status-bar"><span class="carrier">Carrier
    <svg width="11" height="8" viewBox="0 0 11 8"><path d="M5.5 8 L0 2.5 A8 8 0 0 1 11 2.5Z" fill="#222"/></svg></span>
    <span class="time">2:32 PM</span><span class="battery"></span></div>
  <div class="abs top-band"></div>
  <div class="abs back-btn">
    <svg width="18" height="18" viewBox="0 0 18 18"><circle cx="9" cy="9" r="9" fill="#dd5400"/><path d="M13 9H6M9 5L5 9l4 4" stroke="#fff" stroke-width="2" fill="none"/></svg>BACK</div>
  <svg class="abs nav-hex" style="left:150px" viewBox="0 0 25 24"><polygon points="6,1 19,1 24,12 19,23 6,23 1,12" fill="none" stroke="#fff" stroke-width="1"/><path d="M12.5 9v6M9.5 12h6" stroke="#fff"/></svg>
  <svg class="abs nav-hex" style="left:206px" viewBox="0 0 25 24"><polygon points="6,1 19,1 24,12 19,23 6,23 1,12" fill="none" stroke="#fff" stroke-width="1"/><rect x="8" y="9" width="9" height="6" fill="none" stroke="#fff"/></svg>

  <div class="abs row-icon" style="top:100px"><svg width="20" height="14" viewBox="0 0 20 14"><path d="M2 11h16c0-5-3-8-8-8H6" fill="none" stroke="#fff" stroke-width="1.2"/><path d="M2 11l3-5h9" fill="none" stroke="#fff"/></svg></div>
  <div class="abs row-text" style="top:111px;font-size:12px">I need <b>IRONING</b></div>
  <div class="abs rule" style="top:151px"></div>

  <div class="abs row-icon" style="top:164px"><svg width="20" height="20" viewBox="0 0 20 20"><circle cx="10" cy="10" r="8" fill="none" stroke="#fff" stroke-width="1.2"/><path d="M10 5v5h4" fill="none" stroke="#fff" stroke-width="1.2"/></svg></div>
  <div class="abs row-text" style="top:175px;font-size:12px">For 4 hours</div>
  <div class="abs rule" style="top:211px"></div>

  <div class="abs row-icon" style="top:224px"><svg width="20" height="20" viewBox="0 0 20 20"><path d="M3 10a7 7 0 1 0 2-5" fill="none" stroke="#fff" stroke-width="1.2"/><path d="M3 3v3h3M10 6v4l3 2" fill="none" stroke="#fff" stroke-width="1.2"/></svg></div>
  <div class="abs row-text" style="top:229px">Frequency<br>On a weekly basis</div>
  <div class="abs rule" style="top:272px"></div>

  <div class="abs row-icon" style="top:285px"><svg width="20" height="20" viewBox="0 0 20 20"><path d="M3 6c0 6 5 11 11 11l2-2-3-3-2 2c-2-1-4-3-5-5l2-2-3-3z" fill="none" stroke="#fff" stroke-width="1.1"/><circle cx="14" cy="6" r="3.5" fill="none" stroke="#fff"/><path d="M12.5 6l1 1 2-2" fill="none" stroke="#fff"/></svg></div>
  <div class="abs row-text" style="top:290px"><span class="cap">CALL ME ON</span><span class="big">0470315827</span></div>
  <div class="abs rule" style="top:333px"></div>

  <div class="abs row-icon" style="top:345px"><svg width="18" height="16" viewBox="0 0 18 16"><g fill="none" stroke="#fff"><circle cx="3" cy="3" r="1.6"/><circle cx="9" cy="3" r="1.6"/><circle cx="15" cy="3" r="1.6"/><circle cx="3" cy="8" r="1.6"/><circle cx="9" cy="8" r="1.6"/><circle cx="15" cy="8" r="1.6"/><circle cx="3" cy="13" r="1.6"/><circle cx="9" cy="13" r="1.6"/><circle cx="15" cy="13" r="1.6"/></g></svg></div>
  <div class="abs row-text" style="top:350px"><span class="cap">Vouchly client number</span><span class="big">123456789555</span></div>
  <div class="abs rule" style="top:394px"></div>

  <div class="abs row-icon" style="top:407px"><svg width="20" height="18" viewBox="0 0 20 18"><rect x="3" y="2" width="14" height="14" fill="none" stroke="#fff" stroke-width="1.1"/><path d="M3 7h14M3 11h14" stroke="#fff"/></svg></div>
  <div class="abs row-text" style="top:412px"><span class="cap">VAUCHER FORMAT</span>Papier</div>
  <div class="abs rule" style="top:454px"></div>

  <div class="abs row-icon" style="top:467px"><svg width="16" height="20" viewBox="0 0 16 20"><path d="M8 19s-6-7-6-11a6 6 0 0 1 12 0c0 4-6 11-6 11z" fill="none" stroke="#fff" stroke-width="1.2"/><circle cx="8" cy="8" r="2" fill="none" stroke="#fff"/></svg></div>
  <div class="abs row-text" style="top:472px"><span class="cap">AT THIS ADDRESS</span>Rue des Tilleuls 21, 1040 Etterbeek</div>

  <div class="abs send-btn">SEND REQUEST</div>
</section>

<!-- Request status screen -->
<section class="screen screen--status">
  <div class="status-bar"><span class="carrier">Carrier
    <svg width="11" height="8" viewBox="0 0 11 8"><path d="M5.5 8 L0 2.5 A8 8 0 0 1 11 2.5Z" fill="#222"/></svg></span>
    <span class="time">2:32 PM</span><span class="battery"></span></div>
  <div class="abs top-band"></div>
  <div class="abs center-x status-title">REQUEST STATUS</div>

  <div class="abs job-icon" style="top:91px"><svg width="24" height="30" viewBox="0 0 24 30"><path d="M12 2v12M7 14h10l4 13H3z" fill="none" stroke="#fff" stroke-width="1.3"/><path d="M9 18l-2 9M12 18v9M15 18l2 9" stroke="#fff"/></svg></div>
  <div class="abs job-title" style="top:111px">Windows cleaning</div>
  <div class="abs job-line" style="top:148px">3 hours-twice a month</div>
  <div class="abs job-line" style="top:167px">Rue des Tilleuls 21, 1040 BXL</div>
  <div class="abs job-line" style="top:185px">Date: to be implemented...</div>
  <div class="abs pending"><span class="ring">···</span>pending</div>
  <div class="abs" style="left:78px;width:228px;top:243px;border-top:1px solid rgba(255,255,255,.35)"></div>

  <div class="abs job-icon" style="top:271px"><svg width="28" height="20" viewBox="0 0 28 20"><path d="M3 15h22c0-7-4-11-11-11H8" fill="none" stroke="#fff" stroke-width="1.3"/><path d="M3 15l4-7h14" fill="none" stroke="#fff"/></svg></div>
  <div class="abs job-title" style="top:290px">IRONING</div>
  <div class="abs job-line" style="top:328px">4hours- on a weekly basis</div>
  <div class="abs job-line" style="top:347px">Clos des Saules 9, 5150 Floreffe</div>
  <div class="abs job-line" style="top:365px">Date: to be implemented...</div>
  <div class="abs job-line" style="top:384px">Request accepted by agency</div>

  <div class="abs btn btn--accept">ACCEPT</div>
  <div class="abs btn btn--refuse">REFUSE</div>
</section>

</body>
</html>
```